Sheriff Candidate needs a large yard sign

A candidate for Sheriff needs to have a sign to put in front of businesses and houses that advertise her candidacy.

Target Market(s)

Democrats, voters

Industry/Entity Type

Political

Font styles to use
Sans Serif

Colors
34a7d7
3276b5

Requirements
Must have
• Must have her picture
• Must have the words "Elect Dana Whitlock" - I'd like the name Dana to be smaller Whitlock. "Elect" and "Whitlock" should be the focus.
• at the bottom in a box "Paid for by the Committee to Elect Dana Whitlock"
Nice to have
• it would be good to have her logo as well.
• blue color for democrats and on a white background
Should not have
• pink color

```html
<!DOCTYPE html>
<html lang="en">
<head>
<meta charset="utf-8">
<title>Elect Dana Whitlock – Yard Sign</title>
<link href="https://fonts.googleapis.com/css2?family=Open+Sans:wght@300;400;700;800&display=swap" rel="stylesheet">
<style>
  :root {
    --page-bg: #4a4a4a;
    --sign-blue: #3276b5;
    --band-blue: #34a7d7;
    --text-white: #ffffff;
    --seal-gold: #c9a23a;
    --photo-dark: #1c2130;
    --photo-mid: #3a3f4f;
    --photo-light: #b58a72;
  }
  * { margin: 0; padding: 0; box-sizing: border-box; }
  html, body {
    width: 1200px;
    height: 742px;
    overflow: hidden;
    background: var(--page-bg);
    font-family: "Open Sans", Arial, sans-serif;
  }
  .canvas {
    position: relative;
    width: 1200px;
    height: 742px;
  }
  .sign {
    position: absolute;
    left: 64px;
    top: 108px;
    width: 1072px;
    height: 554px;
    background: var(--sign-blue);
    overflow: hidden;
  }
  .headline {
    position: absolute;
    left: 68px;
    color: var(--text-white);
    line-height: 1;
    white-space: nowrap;
  }
  .headline--elect {
    top: 42px;
    font-size: 162px;
    font-weight: 800;
    letter-spacing: -2px;
  }
  .headline--first {
    top: 188px;
    font-size: 116px;
    font-weight: 300;
    letter-spacing: -2px;
  }
  .headline--last {
    top: 300px;
    font-size: 108px;
    font-weight: 800;
    letter-spacing: -3px;
  }
  .campaign-mark {
    position: absolute;
    left: 524px;
    top: 150px;
    width: 152px;
    display: flex;
    flex-direction: column;
    align-items: center;
    gap: 10px;
  }
  .campaign-mark__dot {
    width: 64px;
    height: 64px;
    border-radius: 50%;
    background: var(--seal-gold);
    flex: none;
  }
  .campaign-mark__name {
    color: var(--text-white);
    font-size: 14px;
    font-weight: 700;
    line-height: 1.25;
    text-align: center;
    text-transform: uppercase;
    letter-spacing: 0.5px;
  }
  .disclaimer-band {
    position: absolute;
    left: 0;
    top: 438px;
    width: 696px;
    height: 98px;
    background: var(--band-blue);
    color: var(--text-white);
    padding: 18px 0 0 68px;
    font-size: 25px;
    font-weight: 300;
    line-height: 36px;
    text-transform: uppercase;
  }
  .disclaimer-band strong { font-weight: 700; }
  .candidate-photo {
    position: absolute;
    left: 756px;
    top: 37px;
    width: 380px;
    height: 625px;
    border-radius: 150px 150px 0 0;
    background: linear-gradient(180deg, var(--photo-light) 0%, var(--photo-light) 30%, var(--photo-mid) 45%, var(--photo-dark) 100%);
  }
</style>
</head>
<body>
<main class="canvas">
  <section class="sign" aria-label="Yard sign: Elect Dana Whitlock">
    <div class="headline headline--elect">ELECT</div>
    <div class="headline headline--first">DANA</div>
    <div class="headline headline--last">WHITLOCK</div>

    <div class="campaign-mark">
      <span class="campaign-mark__dot"></span>
      <span class="campaign-mark__name">Whitlock<br>for Sheriff</span>
    </div>

    <div class="disclaimer-band">
      Paid for by the<br>
      Committee to <strong>Elect Dana Whitlock</strong>
    </div>
  </section>
  <div class="candidate-photo" role="img" aria-label="Portrait of candidate Dana Whitlock smiling, wearing a dark blazer over a patterned blouse"></div>
</main>
</body>
</html>
```